Plant Grower/Nursery needs a fun, professional and fresh 1/2 page print ad for a high profile gar...

We need a print ad for a garden tour geared towards plant enthusiasts that support California Native, natural and sustainable plants. A good percentage of our target market want a conservation and earth friendly approach to gardens/landscaping. We want to target this market, as well as, people who are looking for a pretty/colorful landscape that require little water/maintenance. **PLEASE LET US KNOW IF YOU HAVE QUESTIONS OR NEED MORE INFORMATION. WE ALSO HAVE MANY MORE PICTURES IF THESE DON'T WORK FOR YOUR DESIGN. ***THE AD CAN HAVE AS FEW AS 1 PHOTO - WE ARE POSTING SEVERAL IN HOPES THAT YOU CAN FIND WHAT IS PERFECT FOR YOUR IDEA!!Thank you

Target Market(s)

Gardeners, Landscapers, Landscape Designers/Architects, Cities and Municipalities.

Industry/Entity Type

Agriculture

Font styles to use
Serif
Sans Serif

Colors

Requirements
Must have
• We believe in growing regionally appropriate plants for Southern California that beatify our natural and urban landscapes.
• For over 20 years, our owners and staff take pride in providing timely, expert, and honest service.
Nice to have
• At least 1 photo. Eye catchy with a modern earthy feel.
• Hundreds of species/hybrids in stock of California Natives, Succulents, Ornamental Grasses, Standard Stock Items and Unique Plants.

```html
<!DOCTYPE html>
<html lang="en">
<head>
<meta charset="utf-8">
<title>Gardening and Landscaping Tour – Half Page Ad</title>
<link href="https://fonts.googleapis.com/css2?family=Playfair+Display:wght@700&family=Crimson+Pro:wght@400;700&family=Lobster&display=swap" rel="stylesheet">
<style>
  :root {
    --page-bg: #d6d6d6;
    --teal: #17a3c6;
    --purple: #8a0ff0;
    --lime: #dcf200;
    --sky: #16b9ee;
    --title-yellow: #e4f23a;
    --white: #ffffff;
    --ink: #1a1a1a;
  }
  * { margin: 0; padding: 0; box-sizing: border-box; }
  html, body {
    width: 920px; height: 1200px; overflow: hidden;
    background: var(--page-bg);
  }
  .ad {
    position: absolute; left: 20px; top: 315px;
    width: 880px; height: 569px;
    overflow: hidden;
    box-shadow: 0 4px 14px rgba(0,0,0,0.35);
  }
  .ad-shapes { position: absolute; inset: 0; width: 100%; height: 100%; }
  .ad p, .headline { white-space: nowrap; }
  .headline {
    position: absolute; left: 53px; top: 38px;
    font-family: "Playfair Display", Georgia, serif;
    font-weight: 700; color: var(--title-yellow);
    font-size: 46px; line-height: 50px;
  }
  .headline .small { font-size: 23px; }
  .belief {
    position: absolute; left: 53px; top: 210px;
    font-family: "Crimson Pro", Georgia, serif; font-weight: 700;
    color: var(--white); font-size: 17px; line-height: 22.4px;
  }
  .service {
    position: absolute; left: 53px; top: 334px;
    font-family: "Crimson Pro", Georgia, serif; color: var(--white);
    font-size: 16px; line-height: 19.5px;
  }
  .service .lead { font-size: 22px; font-weight: 700; }
  .stock {
    position: absolute; left: 53px; top: 407px;
    font-family: "Crimson Pro", Georgia, serif; font-weight: 700;
    color: var(--white); font-size: 15px; line-height: 22px;
  }
  .call {
    position: absolute; left: 53px; top: 493px;
    font-family: "Lobster", cursive; color: var(--ink);
    font-size: 34px; line-height: 40px;
  }
</style>
</head>
<body>
  <section class="ad">
    <svg class="ad-shapes" viewBox="0 0 786 508" preserveAspectRatio="none">
      <defs>
        <linearGradient id="foliage" x1="0" y1="0" x2="0" y2="1">
          <stop offset="0" stop-color="#6f8a3c"/>
          <stop offset="0.5" stop-color="#557a2e"/>
          <stop offset="1" stop-color="#4d6c2c"/>
        </linearGradient>
        <radialGradient id="blooms" cx="0.6" cy="0.55" r="0.55">
          <stop offset="0" stop-color="#8a5ad0" stop-opacity="0.85"/>
          <stop offset="1" stop-color="#8a5ad0" stop-opacity="0"/>
        </radialGradient>
      </defs>
      <rect class="teal-field" width="786" height="508" fill="var(--teal)"/>
      <rect class="purple-band" x="0" y="283" width="460" height="149" fill="var(--purple)"/>
      <rect class="lime-band" x="0" y="432" width="460" height="46" fill="var(--lime)"/>
      <path class="sky-sweep" d="M366,0 C330,110 330,200 370,290 C395,350 395,440 385,508 L786,508 L786,0 Z" fill="var(--sky)"/>
      <path class="white-edge" d="M370,0 C334,110 336,200 376,285 C411,360 421,440 424,508 L786,508 L786,0 Z" fill="var(--white)"/>
      <path class="lime-sweep" d="M374,0 C338,110 340,200 380,285 C415,360 425,440 428,508 L786,508 L786,0 Z" fill="var(--lime)"/>
      <path class="white-edge" d="M463,0 C410,90 395,200 415,300 C430,380 440,450 445,508 L786,508 L786,0 Z" fill="var(--white)"/>
      <g role="img" aria-label="Photo of purple penstemon flowers blooming among green foliage">
        <path d="M468,0 C415,90 400,200 420,300 C435,380 445,450 450,508 L786,508 L786,0 Z" fill="url(#foliage)"/>
        <path d="M468,0 C415,90 400,200 420,300 C435,380 445,450 450,508 L786,508 L786,0 Z" fill="url(#blooms)"/>
      </g>
    </svg>

    <h1 class="headline">Gardening <span class="small">and</span><br>Landscaping<br>Tour</h1>

    <p class="belief">We believe in growing regionally<br>appropriate plants for Southern California<br>that beatify our natural and<br>urban landscapes.</p>

    <p class="service"><span class="lead">For over 20 years</span>, our owners<br>and staff take pride in providing timely, expert,<br>and honest service</p>

    <p class="stock">Hundreds of species/hybrids in stock of<br>California Natives, Succulents, Ornamental Grasses,<br>Standard Stock Items and Unique Plants.</p>

    <p class="call">Call Us : 0148 372 905</p>
  </section>
</body>
</html>
```